Project Title:
Zembrix – Company Management Platform UI Design
Project Overview:
We are developing Zembrix, an all-in-one management platform for professional product and sales. The software combines daily operations, cost management, inventory, personnel administration, and planning into a single system.
We are launching this design competition to receive a clean, modern UI design that reflects the efficiency and structure of our system. This is not a Point of Sale (POS) system, but rather a back-office/administration tool used by product, sales, and office teams.
What we need:
A dashboard + 7 core module pages. The design should be dark, minimalist, and optimized for desktop views.
Dashboard Requirements:
The dashboard is the first screen after login. It should display:
• Due Dates
o Birthdays
o Passport expirations
o Contract expirations
o Residence permit expiration
o Missing documents / confirmations
o Vacation
o Illness
o Absence
o Warnings
o Terminations
o Maintenance
• Daily Routine
o Tasks
o Appointments
o Holidays & special days
o Vehicle logbook
o Deadlines
o To-do lists
o Weather
• Reports Shortcut
o Income and expenses
• Financial Overview
o Finances (income/expenses)
o Target-actual planning
o EBIT – target-actual
o OPDS documentation
o Loaned items
o Inventory
o Inventory price difference
o Contracts
o Reimbursements
o Travel expenses
7 Main Modules:
1. Activities – Daily closing, documentation, company data
2. Planning – Personnel, supplier, and service planning
3. Files – Personnel files, supplier data, service contracts
4. Costs – Personnel, supplier, and service costs
5. Finances – Income/expenses, EBIT balance sheet, liquidity overview
6. Product Goods – Inventory, price comparison, orders
7. API / Settings – Basic settings, interfaces, calendar, contacts
User Groups:
• Production roles: A, B, C…
• Office roles: A, B, C…
• Management: A, B, C…
Design Preferences:
• Style: Modern, minimalist, functional
• Theme: Dark/Light mode (standard and negative)
• Colors: Dark blue, gold/black accents, neon green
• Layout: Modular blocks, icons + labels, high readability, statistical charts
Deliverables:
• UI design files (Figma preferred, XD or Sketch acceptable)
• Static screens only (no prototype required)
• Up to 8 screens: 1 dashboard + 7 modules
Note:
This design will form the visual foundation of our product. We are looking for clearly structured, clean layouts that help companies manage their operations efficiently.

```html
<!DOCTYPE html>
<html lang="en">
<head>
<meta charset="utf-8">
<title>Zembrix – Dashboard</title>
<link href="https://fonts.googleapis.com/css2?family=Poppins:wght@400;500;600;700;800&display=swap" rel="stylesheet">
<style>
:root{
  --bg:#0b1b4d;
  --panel:#10245a;
  --panel-2:#142a66;
  --row:#0d1f52;
  --line:#23397a;
  --text:#ffffff;
  --muted:#9fb0d8;
  --gold:#e3b23c;
  --green:#3cff1f;
  --red:#ff4b4b;
}
*{box-sizing:border-box;margin:0;padding:0}
html,body{width:1195px;height:1200px;overflow:hidden}
body{background:var(--bg);font-family:'Poppins',sans-serif;color:var(--text);position:relative}
.abs{position:absolute}
svg{display:block}

/* sidebar */
.sidebar{left:17px;top:20px;width:167px;height:1147px;background:linear-gradient(180deg,#10245a 0%,#10245a 70%,#0f3a3f 100%);border:1px solid var(--line);border-radius:16px}
.brand{position:absolute;left:28px;top:18px}
.brand-name{font-weight:700;font-size:22px;line-height:1}
.brand-sub{font-size:9px;font-weight:500;margin-top:4px}
.nav{position:absolute;left:18px;top:80px;width:131px;list-style:none}
.nav li{height:36px;display:flex;align-items:center;gap:10px;padding-left:12px;font-size:9.5px;font-weight:500}
.nav li.active{background:var(--gold);border-radius:18px;font-weight:600;margin-bottom:8px}
.nav svg{width:15px;height:15px;stroke:#fff;fill:none;stroke-width:1.5}
.user{position:absolute;left:13px;top:1059px;width:140px;height:72px;background:var(--panel-2);border-radius:14px;display:flex;align-items:center;gap:8px;padding:0 12px;border:1px solid var(--line)}
.avatar{width:28px;height:28px;border-radius:50%;background:linear-gradient(135deg,#c9d3e8,#6b7a99)}
.user-name{font-size:9.5px;font-weight:600}
.user-handle{font-size:8px;color:var(--muted)}
.user svg{margin-left:auto;width:10px;height:14px;stroke:#fff;fill:none;stroke-width:1.4}

/* top bar */
.search{left:210px;top:20px;width:269px;height:35px;background:var(--panel);border-radius:18px;display:flex;align-items:center;padding-left:21px;font-size:8.5px;color:var(--muted)}
.search-btn{position:absolute;right:2px;top:3px;width:29px;height:29px;border-radius:50%;background:var(--gold);display:flex;align-items:center;justify-content:center}
.icon-btn{top:18px;width:38px;height:38px;border-radius:50%;border:1px solid #5a6fa8;display:flex;align-items:center;justify-content:center}
.icon-btn svg{width:16px;height:16px;stroke:#fff;fill:none;stroke-width:1.5}
.dot{position:absolute;top:9px;right:9px;width:5px;height:5px;border-radius:50%}

/* hero */
.hero{left:212px;top:78px;width:961px;height:99px;border-radius:16px;border:1px solid #3c5aa8;background:linear-gradient(100deg,#0f3a48 0%,#12285e 40%,#1a3f9a 70%,#2455c4 100%);overflow:hidden}
.hero-icon{position:absolute;left:34px;top:28px;width:44px;height:44px;border-radius:50%;background:#0b1838;display:flex;align-items:center;justify-content:center}
.hero-title{position:absolute;left:92px;top:20px;font-size:30px;font-weight:700;line-height:1.1}
.hero-sub{position:absolute;left:93px;top:58px;font-size:12px}
.role-label{position:absolute;left:735px;top:42px;font-size:9px;font-weight:600}
.role-select{position:absolute;left:792px;top:31px;width:131px;height:35px;background:#fff;border-radius:18px;color:#0b1b4d;font-size:9px;font-weight:500;display:flex;align-items:center;padding:0 14px;justify-content:space-between}

/* cards */
.card{background:var(--panel);border-radius:16px;border:1px solid #1b3272}
.card-head{position:absolute;left:30px;top:22px}
.card-title{font-size:16px;font-weight:700}
.card-sub{font-size:9.5px;color:#cdd6ee;margin-top:2px}
.card-link{position:absolute;right:19px;top:36px;font-size:8.5px;font-weight:700;color:var(--gold);text-decoration:underline}

.due{left:212px;top:212px;width:310px;height:458px}
.due-list{position:absolute;left:26px;top:86px;width:265px}
.due-row{height:48.5px;border-radius:8px;display:flex;align-items:center;padding:0 20px;gap:16px}
.due-row.shade{background:var(--row)}
.due-row svg{width:22px;height:22px;stroke:#8fa2cf;fill:none;stroke-width:1.2;flex:none}
.row-title{font-size:10px;font-weight:500}
.row-sub{font-size:8px;color:var(--muted)}
.pill{margin-left:auto;font-size:7.5px;font-weight:600;padding:2px 10px;border-radius:10px;border:1px solid}
.pill.gold{color:var(--gold);border-color:var(--gold);background:#2a2a2a55}
.pill.green{color:var(--green);border-color:var(--green);background:#0d3a2255}
.pill.red{color:var(--red);border-color:var(--red);background:#3a1a2a55}
.scroll{position:absolute;width:3px;height:46px;border-radius:2px;background:#5a6fa8}

.daily{left:537px;top:212px;width:309px;height:458px}
.daily-list{position:absolute;left:28px;top:78px;width:252px}
.daily-row{height:62px;border-bottom:1px solid var(--line);display:flex;align-items:center;gap:16px;padding-left:2px}
.daily-row svg{width:20px;height:20px;stroke:#8fa2cf;fill:none;stroke-width:1.2;flex:none}
.time{margin-left:auto;font-size:8px;color:var(--muted)}

.report{left:862px;top:212px;width:311px;height:324px}
.report .card-head{left:0;right:0;text-align:center}
.tiles{position:absolute;left:50px;top:75px;display:grid;grid-template-columns:100px 100px;gap:10px}
.tile{height:100px;border-radius:12px;border:1px solid #2a4386;display:flex;flex-direction:column;align-items:center;justify-content:center;text-align:center;gap:3px}
.tile svg{width:16px;height:16px;stroke:#fff;fill:none;stroke-width:1.4;margin-bottom:6px}
.tile-name{font-size:9.5px;font-weight:600;line-height:1.3}
.tile-sub{font-size:8px;color:var(--muted)}
.t1{background:linear-gradient(160deg,#10245a 30%,#1a6a8c 100%)}
.t2{background:linear-gradient(200deg,#7a1a3a 0%,#10245a 60%)}
.t3{background:linear-gradient(200deg,#8a7432 0%,#10245a 60%)}
.t4{background:linear-gradient(200deg,#1f9a2c 0%,#10245a 65%)}

.weather{left:862px;top:553px;width:311px;height:117px}
.weather-icon{position:absolute;left:24px;top:18px}
.weather-title{position:absolute;left:120px;top:36px;font-size:16px;font-weight:700}
.weather-sub{position:absolute;left:120px;top:60px;font-size:9px}
.weather-div{position:absolute;left:216px;top:16px;width:1px;height:86px;background:var(--line)}
.temp{position:absolute;left:236px;top:36px;font-size:29px;font-weight:700}

/* financial */
.fin-title{left:212px;top:704px;font-size:16px;font-weight:700}
.fin-sub{left:212px;top:726px;font-size:9.5px;color:#cdd6ee}
.fy{left:1048px;top:715px;font-size:8.5px;font-weight:600}
.export{left:1098px;top:707px;width:75px;height:28px;background:var(--gold);border-radius:14px;font-size:8.5px;font-weight:700;display:flex;align-items:center;justify-content:center}

.chart{top:757px;height:276px}
.chart-title{position:absolute;left:27px;top:22px;font-size:10px}
.c1{left:212px;width:491px}
.c2{left:717px;width:221px}
.c3{left:950px;width:223px}
.legend{font-size:9px;display:flex;gap:12px;align-items:center}
.legend i{display:inline-block;width:7px;height:7px;border-radius:50%;margin-right:5px}
.pct{position:absolute;left:0;right:0;top:208px;text-align:center;font-size:31px;font-weight:700;line-height:1}
.pct-sub{position:absolute;left:0;right:0;top:245px;text-align:center;font-size:9.5px;color:#cdd6ee}

.stat{top:1053px;width:152px;height:70px;display:flex;align-items:center;gap:12px;padding-left:22px}
.stat svg{width:34px;height:34px;stroke:#8fa2cf;fill:none;stroke-width:1.3;flex:none}
.stat-label{font-size:8px;color:#cdd6ee}
.stat-value{font-size:18px;font-weight:700;line-height:1.2}
.note{left:0;right:0;top:1165px;text-align:center;font-size:9.5px;color:#9fb0d8}
</style>
</head>
<body>

<!-- Sidebar -->
<aside class="abs sidebar">
  <div class="brand"><div class="brand-name">Zembrix</div><div class="brand-sub">Management</div></div>
  <ul class="nav">
    <li class="active"><svg viewBox="0 0 24 24"><path d="M4 11l8-7 8 7v9H4z"/><path d="M10 20v-5h4v5"/></svg>Dashboard</li>
    <li><svg viewBox="0 0 24 24"><path d="M3 6l2 2 3-3M3 13l2 2 3-3M11 7h10M11 14h10M4 20h17"/></svg>Activities</li>
    <li><svg viewBox="0 0 24 24"><rect x="3" y="5" width="18" height="16" rx="2"/><path d="M3 10h18M8 3v4M16 3v4M7 14h2M11 14h2M15 14h2M7 17h2M11 17h2"/></svg>Planning</li>
    <li><svg viewBox="0 0 24 24"><rect x="4" y="3" width="16" height="18" rx="3"/><path d="M8 8h8M8 12h8M8 16h5"/></svg>Files</li>
    <li><svg viewBox="0 0 24 24"><rect x="3" y="5" width="18" height="15" rx="2"/><path d="M3 9h14M15 13h6v4h-6z"/></svg>Costs</li>
    <li><svg viewBox="0 0 24 24"><circle cx="12" cy="12" r="9"/><path d="M12 3v9h9"/></svg>Finances</li>
    <li><svg viewBox="0 0 24 24"><path d="M12 3l9 5-9 5-9-5z"/><path d="M3 12l9 5 9-5M3 16l9 5 9-5"/></svg>Product Goods</li>
    <li><svg viewBox="0 0 24 24"><circle cx="12" cy="12" r="3"/><path d="M12 2l2 3 3-1 1 3 3 1-1 3 2 2-2 2 1 3-3 1-1 3-3-1-2 3-2-3-3 1-1-3-3-1 1-3-2-2 2-2-1-3 3-1 1-3 3 1z"/></svg>API / Settings</li>
  </ul>
  <div class="user">
    <div class="avatar" role="img" aria-label="User profile photo"></div>
    <div><div class="user-name">Elian Marsh</div><div class="user-handle">@elianmarsh</div></div>
    <svg viewBox="0 0 10 14"><path d="M2 5l3-3 3 3M2 9l3 3 3-3"/></svg>
  </div>
</aside>

<!-- Top bar -->
<div class="abs search">Search tasks, files, people...
  <div class="search-btn"><svg width="12" height="12" viewBox="0 0 24 24" fill="none" stroke="#fff" stroke-width="2.4"><circle cx="11" cy="11" r="6"/><path d="M16 16l4 4"/></svg></div>
</div>
<div class="abs icon-btn" style="left:1041px"><svg viewBox="0 0 24 24"><circle cx="12" cy="12" r="3"/><path d="M12 2l2 3 3-1 1 3 3 1-1 3 2 2-2 2 1 3-3 1-1 3-3-1-2 3-2-3-3 1-1-3-3-1 1-3-2-2 2-2-1-3 3-1 1-3 3 1z"/></svg></div>
<div class="abs icon-btn" style="left:1088px"><svg viewBox="0 0 24 24"><path d="M4 5h16v11H9l-5 4z"/><path d="M8 10.5h.01M12 10.5h.01M16 10.5h.01"/></svg><span class="dot" style="background:var(--red)"></span></div>
<div class="abs icon-btn" style="left:1135px"><svg viewBox="0 0 24 24"><path d="M6 16V11a6 6 0 0112 0v5l2 2H4z"/><path d="M10 21h4"/></svg><span class="dot" style="background:var(--green)"></span></div>

<!-- Hero -->
<section class="abs hero">
  <div class="hero-icon"><svg width="20" height="20" viewBox="0 0 24 24" fill="none" stroke="#e3b23c" stroke-width="1.8"><path d="M4 11l8-7 8 7v9H4z"/><path d="M10 20v-5h4v5"/></svg></div>
  <h1 class="hero-title">Dashboard</h1>
  <p class="hero-sub">Overview of due dates, routine, reports &amp; financials</p>
  <span class="role-label">Role View</span>
  <div class="role-select">Management A <svg width="10" height="10" viewBox="0 0 10 10" fill="none" stroke="#0b1b4d" stroke-width="1.6"><path d="M2 3.5l3 3 3-3"/></svg></div>
</section>

<!-- Due Dates -->
<section class="abs card due">
  <div class="card-head"><div class="card-title">Due Dates</div><div class="card-sub">HR &amp; compliance reminders</div></div>
  <span class="card-link">VIEW ALL</span>
  <div class="due-list">
    <div class="due-row shade"><svg viewBox="0 0 24 24"><path d="M4 20h16v-6H4zM6 14v-3h12v3M12 11V7M12 5v.01"/></svg><div><div class="row-title">Birthday</div><div class="row-sub">Sara Malik</div></div><span class="pill gold">Oct 18</span></div>
    <div class="due-row"><svg viewBox="0 0 24 24"><rect x="5" y="3" width="14" height="18" rx="2"/><circle cx="12" cy="10" r="3.5"/><path d="M9 17h6"/></svg><div><div class="row-title">Passport Exp.</div><div class="row-sub">Ahmed Khan</div></div><span class="pill gold">Oct 18</span></div>
    <div class="due-row shade"><svg viewBox="0 0 24 24"><path d="M4 20l9-9M14 4a4 4 0 005 5l-2 2-4-4zM4 4l5 5M15 15l5 5"/></svg><div><div class="row-title">Maintenance</div><div class="row-sub">Printer – 3F</div></div><span class="pill green">Today</span></div>
    <div class="due-row"><svg viewBox="0 0 24 24"><rect x="3" y="5" width="18" height="16" rx="2"/><path d="M3 10h18M8 3v4M16 3v4"/><circle cx="12" cy="15" r="2"/></svg><div><div class="row-title">Vacation</div><div class="row-sub">H. Raza</div></div><span class="pill green">This Week</span></div>
    <div class="due-row shade"><svg viewBox="0 0 24 24"><circle cx="12" cy="8" r="4"/><path d="M4 21c0-4 4-7 8-7s8 3 8 7"/></svg><div><div class="row-title">1 Employee</div><div class="row-sub">1 Employee</div></div><span class="pill green">Today</span></div>
    <div class="due-row"><svg viewBox="0 0 24 24"><path d="M12 3l10 18H2z"/><path d="M12 10v5M12 18v.01"/></svg><div><div class="row-title">Warning</div><div class="row-sub">P. Omar</div></div><span class="pill red">Pending</span></div>
    <div class="due-row shade"><svg viewBox="0 0 24 24"><path d="M5 3h10v18H5zM15 12h6M18 9l3 3-3 3"/></svg><div><div class="row-title">Termination</div><div class="row-sub">M. Lee</div></div><span class="pill red">Queued</span></div>
  </div>
  <span class="scroll" style="left:299px;top:202px"></span>
</section>

<!-- Daily Routine -->
<section class="abs card daily">
  <div class="card-head"><div class="card-title">Daily Routine</div><div class="card-sub">Today's plan &amp; log</div></div>
  <span class="card-link">ADD</span>
  <div class="daily-list">
    <div class="daily-row"><svg viewBox="0 0 24 24"><rect x="4" y="3" width="16" height="18" rx="2"/><path d="M8 8h8M8 12h8M8 16h5"/></svg><div><div class="row-title">Approve supplier invoices</div><div class="row-sub">Task</div></div><span class="time">09:30</span></div>
    <div class="daily-row"><svg viewBox="0 0 24 24"><path d="M20 12a8 8 0 01-14 5M4 12a8 8 0 0114-5M18 3v4h-4M6 21v-4h4"/></svg><div><div class="row-title">Ops sync – Q3</div><div class="row-sub">Apointment</div></div><span class="time">09:30</span></div>
    <div class="daily-row"><svg viewBox="0 0 24 24"><rect x="4" y="4" width="14" height="17" rx="2"/><path d="M8 9h6M8 13h6M14 18l2 2 4-4"/></svg><div><div class="row-title">Inventory audit upload</div><div class="row-sub">Holiday</div></div><span class="time">09:30</span></div>
    <div class="daily-row"><svg viewBox="0 0 24 24"><rect x="3" y="5" width="18" height="16" rx="2"/><path d="M3 10h18M8 3v4M16 3v4M7 14h2M11 14h2M15 14h2M7 17h2"/></svg><div><div class="row-title">Founders Day (Office)</div><div class="row-sub">Deadline</div></div><span class="time">09:30</span></div>
    <div class="daily-row"><svg viewBox="0 0 24 24"><rect x="4" y="3" width="16" height="18" rx="2"/><path d="M8 8h8M8 12h8M8 16h5"/></svg><div><div class="row-title">Fleet mileage update</div><div class="row-sub">Vehicle Logbook</div></div><span class="time">09:30</span></div>
    <div class="daily-row"><svg viewBox="0 0 24 24"><path d="M20 12a8 8 0 01-14 5M4 12a8 8 0 0114-5M18 3v4h-4M6 21v-4h4"/></svg><div><div class="row-title">Ops sync – Q4</div><div class="row-sub">Task</div></div><span class="time">09:30</span></div>
  </div>
  <span class="scroll" style="left:298px;top:202px"></span>
</section>

<!-- Report Shortcut -->
<section class="abs card report">
  <div class="card-head"><div class="card-title">Report Shortcut</div><div class="card-sub">Quick Access</div></div>
  <div class="tiles">
    <div class="tile t1"><svg viewBox="0 0 24 24"><rect x="3" y="5" width="18" height="15" rx="2"/><path d="M3 9h14M15 13h6v4h-6z"/></svg><div class="tile-name">Income &amp;<br>Expenses</div><div class="tile-sub">Open report</div></div>
    <div class="tile t2"><svg viewBox="0 0 24 24"><circle cx="12" cy="12" r="9"/><path d="M12 3v9h9"/></svg><div class="tile-name">EBIT<br>Summary</div><div class="tile-sub">Open report</div></div>
    <div class="tile t3"><svg viewBox="0 0 24 24"><rect x="4" y="3" width="16" height="18" rx="3"/><path d="M8 8h8M8 12h8M8 16h5"/></svg><div class="tile-name">Liquidity</div><div class="tile-sub">Open report</div></div>
    <div class="tile t4"><svg viewBox="0 0 24 24"><rect x="3" y="5" width="18" height="15" rx="2"/><path d="M3 9h14M15 13h6v4h-6z"/></svg><div class="tile-name">Reimbursements</div><div class="tile-sub">Open report</div></div>
  </div>
</section>

<!-- Weather -->
<section class="abs card weather">
  <svg class="weather-icon" width="86" height="82" viewBox="0 0 86 82" role="img" aria-label="Partly cloudy weather icon">
    <g stroke="#e3b23c" stroke-width="4" stroke-linecap="round">
      <line x1="52" y1="4" x2="52" y2="10"/>
      <line x1="72" y1="14" x2="68" y2="18"/>
      <line x1="80" y1="32" x2="74" y2="32"/>
      <line x1="32" y1="14" x2="36" y2="18"/>
      <line x1="26" y1="32" x2="31" y2="32"/>
    </g>
    <circle cx="52" cy="33" r="15" fill="#e3b23c"/>
    <g fill="#ffffff">
      <circle cx="24" cy="54" r="14"/>
      <circle cx="42" cy="50" r="16"/>
      <circle cx="56" cy="62" r="11"/>
      <rect x="10" y="56" width="57" height="21" rx="10"/>
    </g>
  </svg>
  <div class="weather-title">Weather</div>
  <div class="weather-sub">Partly cloudy</div>
  <span class="weather-div"></span>
  <div class="temp">33°</div>
</section>

<!-- Financial Overview -->
<h2 class="abs fin-title">Financial Overview</h2>
<p class="abs fin-sub">Finances, planning vs actual, EBIT</p>
<span class="abs fy">FY 2025</span>
<span class="abs export">EXPORT</span>

<section class="abs card chart c1">
  <div class="chart-title">Finances (Income / Expenses)</div>
  <svg class="abs" style="left:0;top:0" width="491" height="276" viewBox="0 0 491 276">
    <defs>
      <linearGradient id="barGreen" x1="0" y1="0" x2="0" y2="1"><stop offset="0" stop-color="#0b1b4d"/><stop offset="1" stop-color="#3cff1f"/></linearGradient>
    </defs>
    <g font-family="Poppins,sans-serif" font-size="7" fill="#cdd6ee">
      <text x="27" y="74">100K</text><text x="30" y="106">80K</text><text x="30" y="138">50K</text><text x="30" y="174">30K</text><text x="30" y="206">20K</text><text x="32" y="235">10K</text>
    </g>
    <g stroke="#3a5090" stroke-dasharray="3 3" stroke-width="0.8">
      <line x1="63" y1="72" x2="468" y2="72"/><line x1="63" y1="104" x2="468" y2="104"/><line x1="63" y1="136" x2="468" y2="136"/><line x1="63" y1="172" x2="468" y2="172"/><line x1="63" y1="204" x2="468" y2="204"/>
    </g>
    <g fill="url(#barGreen)">
      <rect x="63" y="181" width="27" height="62" rx="8"/>
      <rect x="111" y="133" width="27" height="110" rx="8"/>
      <rect x="158" y="100" width="27" height="143" rx="8"/>
      <rect x="205" y="52" width="27" height="191" rx="8"/>
      <rect x="252" y="193" width="27" height="50" rx="8"/>
      <rect x="300" y="134" width="27" height="109" rx="8"/>
      <rect x="347" y="193" width="27" height="50" rx="8"/>
      <rect x="394" y="57" width="27" height="186" rx="8"/>
      <rect x="441" y="134" width="27" height="109" rx="8"/>
    </g>
    <g font-family="Poppins,sans-serif" font-size="7.5" fill="#cdd6ee" text-anchor="middle">
      <text x="67" y="264">Jan</text><text x="124" y="264">Feb</text><text x="171" y="264">Mar</text><text x="218" y="264">Apr</text><text x="268" y="264">May</text><text x="315" y="264">Jun</text><text x="358" y="264">Jul</text><text x="407" y="264">Aug</text><text x="450" y="264">Sep</text>
    </g>
  </svg>
</section>

<section class="abs card chart c2">
  <div class="chart-title" style="left:32px">Target – Actual (Quarterly)</div>
  <svg class="abs" style="left:0;top:0" width="221" height="276" viewBox="0 0 221 276">
    <g stroke="#2c4386" stroke-width="0.7">
      <line x1="47" y1="50" x2="197" y2="50"/><line x1="47" y1="74" x2="197" y2="74"/><line x1="47" y1="100" x2="197" y2="100"/><line x1="47" y1="124" x2="197" y2="124"/><line x1="47" y1="145" x2="197" y2="145"/><line x1="47" y1="168" x2="197" y2="168"/><line x1="47" y1="193" x2="197" y2="193"/><line x1="47" y1="216" x2="197" y2="216"/>
      <line x1="47" y1="50" x2="47" y2="216"/><line x1="82" y1="50" x2="82" y2="216"/><line x1="117" y1="50" x2="117" y2="216"/><line x1="152" y1="50" x2="152" y2="216"/><line x1="197" y1="50" x2="197" y2="216"/>
    </g>
    <g font-family="Poppins,sans-serif" font-size="7" fill="#cdd6ee" text-anchor="end">
      <text x="39" y="77">600</text><text x="39" y="103">500</text><text x="39" y="127">400</text><text x="39" y="148">300</text><text x="39" y="171">200</text><text x="39" y="196">100</text><text x="39" y="219">0</text>
    </g>
    <g stroke-width="3.5" stroke-linecap="round">
      <line x1="61" y1="214" x2="61" y2="117" stroke="#3cff1f"/><line x1="68" y1="214" x2="68" y2="103" stroke="#e3b23c"/>
      <line x1="95" y1="214" x2="95" y2="60" stroke="#3cff1f"/><line x1="102" y1="214" x2="102" y2="71" stroke="#e3b23c"/>
      <line x1="130" y1="214" x2="130" y2="180" stroke="#3cff1f"/><line x1="137" y1="214" x2="137" y2="160" stroke="#e3b23c"/>
      <line x1="164" y1="214" x2="164" y2="116" stroke="#3cff1f"/><line x1="171" y1="214" x2="171" y2="103" stroke="#e3b23c"/>
    </g>
    <g font-family="Poppins,sans-serif" font-size="7" fill="#cdd6ee" text-anchor="middle">
      <text x="65" y="230">Q1</text><text x="99" y="230">Q2</text><text x="133" y="230">Q3</text><text x="168" y="230">Q4</text>
    </g>
  </svg>
  <div class="abs legend" style="left:72px;top:246px"><span><i style="background:var(--green)"></i>Actual</span><span><i style="background:var(--gold)"></i>Plan</span></div>
</section>

<section class="abs card chart c3">
  <div class="chart-title" style="left:33px">EBIT – Target vs Actual</div>
  <div class="abs" style="left:167px;top:22px;font-size:8.5px;line-height:1.9">
    <div><i style="display:inline-block;width:7px;height:7px;border-radius:50%;background:var(--green);margin-right:5px"></i>EBIT</div>
    <div><i style="display:inline-block;width:7px;height:7px;border-radius:50%;background:var(--gold);margin-right:5px"></i>Gap</div>
  </div>
  <svg class="abs" style="left:40px;top:52px" width="142" height="142" viewBox="0 0 142 142">
    <circle cx="71" cy="71" r="64" fill="none" stroke="#ffffff" stroke-width="8"/>
    <circle cx="71" cy="71" r="64" fill="none" stroke="#e3b23c" stroke-width="8" stroke-dasharray="120 402" transform="rotate(-92 71 71)" stroke-linecap="round"/>
    <circle cx="71" cy="71" r="52" fill="none" stroke="#3cff1f" stroke-width="9"/>
  </svg>
  <div class="pct">72%</div>
  <div class="pct-sub">of target achieved</div>
</section>

<!-- Stats -->
<div class="abs card stat" style="left:212px"><svg viewBox="0 0 34 34"><path d="M5 28c4-2 8-1 12 0s9 0 12-3M11 16a6 6 0 1012 0c0-4-3-6-6-10-3 4-6 6-6 10zM17 13v6"/></svg><div><div class="stat-label">Loaned Items</div><div class="stat-value">23</div></div></div>
<div class="abs card stat" style="left:374px"><svg viewBox="0 0 34 34"><rect x="6" y="6" width="22" height="24" rx="2"/><path d="M12 4h10v4H12zM10 14l2 2 3-3M18 15h7M10 22l2 2 3-3M18 23h7"/></svg><div><div class="stat-label">Inventory</div><div class="stat-value">1275</div></div></div>
<div class="abs card stat" style="left:535px"><svg viewBox="0 0 34 34"><circle cx="17" cy="17" r="13"/><path d="M21 12c-1-2-7-2-7 1s7 2 7 6-6 3-8 1M17 8v18"/></svg><div><div class="stat-label">Price Diff.</div><div class="stat-value">+2.4%</div></div></div>
<div class="abs card stat" style="left:698px"><svg viewBox="0 0 34 34"><path d="M8 4h14l5 5v21H8z"/><path d="M12 12h10M12 17h10M12 22h6M20 28l8-8 2 2-8 8h-2z"/></svg><div><div class="stat-label">Contracts</div><div class="stat-value">48</div></div></div>
<div class="abs card stat" style="left:859px"><svg viewBox="0 0 34 34"><rect x="4" y="11" width="26" height="16" rx="2"/><path d="M13 11V7h8v4M9 19h16M20 15l-5 4 5 4"/></svg><div><div class="stat-label">Travel Exp.</div><div class="stat-value">$12.4k</div></div></div>
<div class="abs card stat" style="left:1021px"><svg viewBox="0 0 34 34"><path d="M6 17a11 11 0 106-9.8M6 5v5h5M20 13c-1-2-6-2-6 1s6 2 6 5-5 3-7 1M17 10v14"/></svg><div><div class="stat-label">Reimburse.</div><div class="stat-value">$7.9k</div></div></div>

<p class="abs note">* Demo data. Hook to your API for live OPDS documentation, reimbursements &amp; travel expenses.</p>

</body>
</html>
```